Bref créative
New Corporate Website - Blue Falcons
Blue Falcons - Marketing & Lead Generation
Marketing
Does not yet exist
Blue Falcons is a new Marketing and Sales Lead generation agency specializing in helping companies analyze, pursue and close sales opportunities generated via the Internet. We provide access to our exclusive Blue Falcon Striker platform for capturing and pursing sales opportunities generated via the online platform.
I'd like to showcase a lot of red on this website. This is a new website for a new company we are starting.
The website is to feature both our online web software as well as our consulting services.
High Tech
Red (#aa0000)
Grey (#cccccc)
Verdana
Century Gothic
top
http://www.vortelix.com
http://www.brinaxo.com/en
http://www.quombrel.com
The page should include links for
Navigation
- About Blue Falcons
- Services & Solutions
- Results
- News & Announcements
- Contact Us
Also, an area for current customer's to login
please incorporate the logo of the man riding the horse backwards.

```html
<!DOCTYPE html>
<html lang="en">
<head>
<meta charset="utf-8">
<title>Blue Falcons – Marketing &amp; Lead Generation</title>
<link rel="stylesheet" href="https://fonts.googleapis.com/css2?family=Marcellus&family=Didact+Gothic&family=Open+Sans:ital,wght@0,400;0,700;1,400&display=swap">
<style>
  :root {
    --red: #aa0000;
    --red-deep: #7a0000;
    --red-bright: #c4100f;
    --red-soft: #d23a3a;
    --grey: #cccccc;
    --grey-light: #e4e4e4;
    --grey-mid: #b5b5b5;
    --grey-dark: #6f6f6f;
    --white: #ffffff;
    --quote: #f6d0d0;
  }
  * { margin: 0; padding: 0; box-sizing: border-box; }
  html, body { width: 1200px; height: 821px; overflow: hidden; }
  body {
    position: relative;
    background: var(--grey-light);
    font-family: "Open Sans", sans-serif;
    color: var(--white);
  }
  .backdrop {
    position: absolute; left: 0; top: 0; width: 1200px; height: 745px;
    background: radial-gradient(ellipse at 50% 55%, #f2f2f2 0%, #bdbdbd 55%, #7c7c7c 100%);
  }
  .backdrop-accent {
    position: absolute; left: 0; top: 610px; width: 1200px; height: 135px;
    background: linear-gradient(180deg, rgba(170,0,0,0) 0%, rgba(170,0,0,.55) 100%);
  }
  .top-nav {
    position: absolute; left: 0; top: 0; width: 1200px; height: 60px;
    background: linear-gradient(180deg, var(--red-bright) 0%, var(--red) 60%, var(--red-deep) 100%);
    font-family: "Didact Gothic", sans-serif; font-size: 18px;
  }
  .top-nav a { position: absolute; top: 20px; color: var(--white); text-decoration: none; }
  .panel {
    position: absolute; left: 125px; top: 84px; width: 950px; height: 624px;
    background: linear-gradient(180deg, var(--red-bright) 0%, var(--red) 55%, var(--red-deep) 100%);
    border-radius: 6px;
    box-shadow: 0 4px 18px rgba(0,0,0,.45);
    overflow: hidden;
  }
  .hero {
    position: absolute; left: 0; top: 0; width: 950px; height: 312px;
    background: linear-gradient(180deg, var(--red-soft) 0%, var(--red) 70%, var(--red-deep) 100%);
  }
  .hero-photo {
    position: absolute; left: 0; top: 60px; width: 440px; height: 252px;
    background: radial-gradient(ellipse at 40% 70%, #f4f4f4 0%, #c9c9c9 45%, rgba(200,200,200,0) 80%);
  }
  .brand {
    position: absolute; left: 38px; top: 22px;
    font-family: "Marcellus", serif; font-size: 42px; color: var(--white);
  }
  .hero-title {
    position: absolute; left: 487px; top: 68px;
    font-family: "Marcellus", serif; font-size: 44px; line-height: 58px; font-weight: 400;
  }
  .hero-quote {
    position: absolute; left: 487px; top: 192px; width: 430px;
    font-style: italic; font-size: 18px; line-height: 22px; color: var(--quote);
  }
  .slider-bar {
    position: absolute; left: 780px; top: 292px; width: 170px; height: 20px;
    background: var(--grey); border-top-left-radius: 10px;
    display: flex; align-items: center; gap: 6px; padding-left: 44px;
  }
  .slider-bar .dot { width: 12px; height: 12px; border-radius: 50%; background: var(--grey-dark); }
  .slider-bar .dot.active { background: var(--red-deep); }
  .hero-rule { position: absolute; left: 0; top: 312px; width: 950px; height: 3px; background: var(--red-deep); }
  .login { position: absolute; left: 38px; top: 340px; width: 230px; }
  .section-title { font-weight: 700; font-size: 26px; line-height: 32px; }
  .field { display: flex; align-items: center; margin-top: 10px; font-size: 13px; font-weight: 700; }
  .field label { width: 110px; }
  .field span { width: 110px; height: 18px; background: var(--grey); border: 1px solid var(--grey-mid); }
  .login-actions { display: flex; gap: 6px; margin: 16px 0 0 86px; }
  .btn {
    font-size: 13px; padding: 1px 8px; border: 1px solid var(--grey);
    background: var(--red-deep); color: var(--white);
  }
  .news { position: absolute; left: 300px; top: 340px; width: 620px; }
  .news-item { margin-top: 12px; font-size: 12.5px; line-height: 15px; font-style: italic; color: var(--quote); }
  .news-item b { font-style: normal; color: var(--white); margin-right: 10px; }
  .footer {
    position: absolute; left: 0; top: 745px; width: 1200px; height: 40px;
    background: var(--grey); color: var(--grey-dark); font-size: 12.5px;
  }
  .footer .copyright { position: absolute; left: 128px; top: 12px; }
  .footer nav { position: absolute; left: 540px; top: 12px; display: flex; gap: 18px; }
  .footer a { color: var(--grey-dark); text-decoration: none; }
</style>
</head>
<body>
  <div class="backdrop" role="img" aria-label="Grey photographic backdrop of stacked three-dimensional internet words"></div>
  <div class="backdrop-accent"></div>

  <nav class="top-nav">
    <a href="#" style="left:166px">About Blue Falcons</a>
    <a href="#" style="left:385px">Services &amp; Solutions Results</a>
    <a href="#" style="left:680px">News &amp; Announcements</a>
    <a href="#" style="left:943px">Contact Us</a>
  </nav>

  <main class="panel">
    <section class="hero">
      <div class="hero-photo" role="img" aria-label="Photo of a single red sphere standing out among rows of white spheres"></div>
      <div class="brand">Blue Falcons</div>
      <h1 class="hero-title">Blue Falcons<br>Lead Generation</h1>
      <p class="hero-quote">“Lorem ipsum dolor sit amet, consectetur adipisicing elit, sed do eiusmod tempor incididunt ut labore et dolore magna aliqua.”</p>
      <div class="slider-bar">
        <span class="dot active"></span><span class="dot"></span><span class="dot"></span><span class="dot"></span><span class="dot"></span>
      </div>
    </section>
    <div class="hero-rule"></div>

    <section class="login">
      <h2 class="section-title">User login</h2>
      <div class="field"><label>User name:</label><span></span></div>
      <div class="field"><label>Password:</label><span></span></div>
      <div class="login-actions"><span class="btn">Login</span><span class="btn">Register</span></div>
    </section>

    <section class="news">
      <h2 class="section-title">News &amp; Announcements</h2>
      <p class="news-item"><b>27 07 2011</b>“Lorem ipsum dolor sit amet, consectetur adipisicing elit, sed do eiusmod tempor incididunt ut labore et dolore magna aliqua. Ut enim ad minim veniam, quis nostrud exercitation ullamco laboris nisi ut aliquip ex ea commodo consequat.”</p>
      <p class="news-item"><b>27 07 2011</b>Duis aute irure dolor in reprehenderit in voluptate velit esse cillum dolore eu fugiat nulla pariatur. Excepteur sint occaecat cupidatat non proident, sunt in culpa qui officia deserunt mollit anim id est laborum.</p>
      <p class="news-item"><b>26 07 2011</b>The standard chunk of Lorem Ipsum used since the 1500s is reproduced below for those interested. Sections 1.10.32 and 1.10.33 from “de Lumine Portarum et Viarum” by Varnel Ostrik are also reproduced in their exact original form, accompanied by English versions from the 1914 translation by T. Dellwyn.</p>
      <p class="news-item"><b>25 07 2011</b>1.10.32 and 1.10.33 of “de Lumine Portarum et Viarum” (The Lights of Gates and Roads) by Varnel Ostrik, written in 45 BC.</p>
    </section>
  </main>

  <footer class="footer">
    <span class="copyright">Copyright © 2011 Blue Falcons. All Rights Reserved</span>
    <nav>
      <a href="#">About Blue Falcons</a>
      <a href="#">Services &amp; Solutions</a>
      <a href="#">Results</a>
      <a href="#">News &amp; Announcements</a>
      <a href="#">Contact Us</a>
    </nav>
  </footer>
</body>
</html>
```